Business Card Design/Stationary Design

We would like designers to submit cool, hip business card designs (plus stationary designs) for a new, upstart software development company located in Toronto.
If you have any questions, please email us.
For inspiration on designs:
http://cardmuse.example/cool-business-cards/
http://layoutnotes.example/2008/05/36-cool-business-cards-you-should%E2%80%99ve-seen.html
http://gigharbor.example/general/18-smokin-hot-business-card-designs/

Card info:

Selvakumar (Selv) Nadarasan

Founder and CEO

47 Brindle Court, Suite 311

Toronto, ON M4K 2T8

Phone: 647-512-7730

Mobile: 416-273-5094

Fax: 647-512-7731

Email: selvakumar.nadarasan@mailbrook.example

www.quendrix.example
Updates

Hi everyone,

In terms of all the designs I have seen so far, here is what I like:

1.  I really like the "back" part of this design.  The "front" looks pretty decent as well, but for the "front", look at #2 on this list.  I like that.

http://www.pitchboard.example/image.aspx?imageLocation=1000_10001_2000_image.jpg&type=design300px&whiteLabelCustId=9999

2. "Side 1" of this I like, the front needs to be reworked.

http://www.pitchboard.example/image.aspx?imageLocation=1000_10002_2000_image.png&type=design300px&whiteLabelCustId=9999

3. http://www.pitchboard.example/image.aspx?imageLocation=1000_10003_2000_image.jpg&type=design300px&whiteLabelCustId=9999

4. http://www.pitchboard.example/image.aspx?imageLocation=1000_10004_2000_image.jpg&type=design300px&whiteLabelCustId=9999

Target Market(s)

We are focused on enterprise customers right now, so businesses with a long-term goal of also reaching out to the consumer market as well.

Industry/Entity Type

Software

Requirements
Must have
• Must look cool, ultra-modern, clean and eye-catching. Must incorporate our logo and the colors found in the logo.

```html
<!DOCTYPE html>
<html lang="en">
<head>
<meta charset="utf-8">
<title>Quendrix Business Card</title>
<link rel="stylesheet" href="https://fonts.googleapis.com/css2?family=Arimo:wght@400;700&display=swap">
<style>
  :root {
    --brand-green: #7db41d;
    --ink: #2b2b2b;
    --ink-soft: #444444;
    --paper: #ffffff;
    --outline: #1a1a1a;
  }
  html, body {
    margin: 0;
    padding: 0;
    width: 1200px;
    height: 1200px;
    overflow: hidden;
    background: var(--paper);
  }
  .canvas {
    position: relative;
    width: 1200px;
    height: 1200px;
    font-family: "Arimo", Arial, sans-serif;
  }
  .card-shapes {
    position: absolute;
    inset: 0;
  }
  .brand {
    position: absolute;
    left: 165px;
    top: 118px;
    display: flex;
    align-items: center;
    gap: 16px;
  }
  .brand-dot {
    width: 96px;
    height: 96px;
    border-radius: 50%;
    background: var(--brand-green);
  }
  .brand-text {
    display: flex;
    flex-direction: column;
    align-items: flex-end;
  }
  .brand-name {
    font-size: 66px;
    font-weight: 400;
    color: var(--ink);
    line-height: 1;
    letter-spacing: 1px;
  }
  .brand-tagline {
    font-size: 11px;
    color: var(--ink-soft);
    letter-spacing: 1.5px;
    margin-top: 4px;
  }
  .holder {
    position: absolute;
    right: 127px;
    top: 124px;
    text-align: right;
  }
  .holder-name {
    font-size: 28px;
    font-weight: 700;
    color: var(--ink);
    line-height: 34px;
  }
  .holder-title {
    font-size: 23px;
    color: var(--ink-soft);
    line-height: 30px;
  }
  .contact {
    position: absolute;
    right: 127px;
    top: 268px;
    text-align: right;
    color: var(--paper);
    font-size: 21.5px;
    line-height: 26.5px;
  }
  .contact p { margin: 0; }
  .contact .address { margin-bottom: 26px; }
</style>
</head>
<body>
<div class="canvas">
  <svg class="card-shapes" width="1200" height="1200" viewBox="0 0 1200 1200" aria-hidden="true">
    <defs>
      <clipPath id="front-card-clip">
        <path d="M149 0 H1039 Q1099 0 1099 60 V547 H209 Q149 547 149 487 Z"/>
      </clipPath>
    </defs>
    <!-- Front side -->
    <g class="front-card" clip-path="url(#front-card-clip)">
      <rect x="149" y="0" width="950" height="547" fill="var(--brand-green)"/>
      <rect class="front-logo-band" x="149" y="84" width="950" height="149" fill="var(--paper)"/>
    </g>
    <!-- Back side -->
    <g class="back-card">
      <path d="M209 648 H1039 Q1099 648 1099 708 V1195 H149 V708 Q149 648 209 648 Z" fill="var(--paper)"/>
      <rect class="back-band" x="149" y="746" width="950" height="135" fill="var(--brand-green)"/>
      <path d="M209 648 H1039 Q1099 648 1099 708 V1195 H149 V708 Q149 648 209 648 Z" fill="none" stroke="var(--outline)" stroke-width="3"/>
    </g>
  </svg>

  <div class="brand">
    <div class="brand-dot"></div>
    <div class="brand-text">
      <span class="brand-name">Quendrix</span>
      <span class="brand-tagline">TECHNOLOGIES INC.</span>
    </div>
  </div>

  <div class="holder">
    <div class="holder-name">Selvakumar (Selv) Nadarasan</div>
    <div class="holder-title">Founder and CEO</div>
  </div>

  <div class="contact">
    <div class="address">
      <p>47 Brindle Court, Suite 311</p>
      <p>Toronto, ON M4K 2T8</p>
    </div>
    <p>Phone: 647.512.7730</p>
    <p>Mobile: 416.273.5094</p>
    <p>Fax: 647.512.7731</p>
    <p>E-mail: selvakumar.nadarasan@mailbrook.example</p>
    <p>www.quendrix.example</p>
  </div>
</div>
</body>
</html>
```